Design business cards and letterhead for real estate company

I need some graphic design. I would like someone to design business cards and letterhead for a real estate company. The logo is attached.

Two sided full color business cards.

The business cards needs the following on it:

Name: Peter Hollis
Position: Broker
Cell: 412-590-6637
Office: 415-203-9916 Ext: 101
Fax: 419-562-0174
Email: peterhollis@[login to view URL]
Website: [login to view URL]
Address: 457 Birchwood Lane
Millbrook, NY 12545

Pictures that need to be on it:
Logo
Agents Picture
Homevest Logo
MLS Logo
Multimillion dollar producer logo: this logo will not be on all business cards so the card needs to look nice with it and without it

Letterhead needs to have:
Logo
Address
Office phone: 413-826-4105
Fax: 417-945-2208
Email: contact@[login to view URL]

```html
<!DOCTYPE html>
<html lang="en">
<head>
<meta charset="utf-8">
<title>Harborline Realty – Stationery Set</title>
<link href="https://fonts.googleapis.com/css2?family=Montserrat:wght@500;600;700;800&family=Open+Sans:ital,wght@0,400;0,600;0,700;1,700&display=swap" rel="stylesheet">
<style>
  :root{
    --red:#e8262d;
    --ink:#1b1b1d;
    --charcoal:#2f3136;
    --slate:#3c3f46;
    --mist:#e4e5e8;
    --paper:#ffffff;
    --stage:#1d1d1f;
    --text:#3a3a3a;
  }
  *{margin:0;padding:0;box-sizing:border-box}
  html,body{width:1200px;height:737px;overflow:hidden;background:var(--stage)}
  .canvas{position:relative;width:1200px;height:737px;overflow:hidden;background:var(--stage);font-family:"Open Sans",Arial,sans-serif;color:var(--text)}

  .brand{font-family:"Montserrat",Arial,sans-serif;font-weight:800;color:var(--ink);line-height:.95;letter-spacing:.3px;text-transform:uppercase;white-space:nowrap}
  .brand span{display:block}

  /* ---------- Letterhead ---------- */
  .letterhead{position:absolute;left:155px;top:35px;width:475px;height:671px;background:var(--paper);overflow:hidden}
  .letterhead__top{position:absolute;left:0;top:0}
  .letterhead .brand{position:absolute;left:42px;top:66px;font-size:16px}
  .letterhead__date{position:absolute;right:40px;top:80px;font-size:6.5px;font-weight:700;font-style:italic;color:var(--ink)}
  .recipient{position:absolute;left:66px;top:158px;font-size:5.4px;line-height:7px;color:var(--ink);font-style:normal}
  .recipient__to{font-size:6px}
  .recipient__name{color:var(--red);font-weight:700;font-size:7px;line-height:9px}
  .letter-body{position:absolute;left:66px;top:236px;width:346px;font-size:5.6px;line-height:8.4px;color:var(--text)}
  .letter-body p{margin-bottom:7px}
  .signature{position:absolute;left:66px;top:528px;color:var(--ink)}
  .signature__name{font-size:7.5px;font-weight:700;font-style:italic}
  .signature__role{font-size:4.5px}
  .letter-contacts{position:absolute;left:42px;top:581px;list-style:none}
  .letter-contacts li{display:flex;align-items:center;gap:12px;font-size:8.5px;height:15px;color:var(--ink);font-family:"Montserrat",Arial,sans-serif;font-weight:500}
  .badges{position:absolute;display:flex;gap:6px;align-items:flex-end}
  .letterhead .badges{left:312px;top:584px}
  .badge{background:var(--paper);border:3px solid var(--ink)}
  .letterhead__footer{position:absolute;left:0;bottom:0}
  .letterhead__web{position:absolute;left:42px;top:650px;display:flex;align-items:center;gap:10px;font-family:"Montserrat",Arial,sans-serif;font-size:8px;font-weight:600;color:var(--paper)}

  /* ---------- Card front ---------- */
  .card{position:absolute;background:var(--paper);overflow:hidden}
  .card--front{left:720px;top:79px;width:411px;height:246px}
  .card--front .brand{position:absolute;left:130px;top:12px;font-size:13px}
  .card__shapes{position:absolute;left:0;top:0}
  .photo{position:absolute;border-radius:50%}
  .photo--agent{left:253px;top:47px;width:146px;height:146px;background:radial-gradient(circle at 55% 60%,#2e3748 0%,#4d5a6c 45%,#b7c3cf 100%);border:3px solid var(--paper)}
  .agent{position:absolute;left:27px;top:46px}
  .agent__name{font-family:"Montserrat",Arial,sans-serif;font-size:13px;font-weight:700;color:var(--red)}
  .agent__role{font-size:7.5px;font-weight:600;color:var(--ink);margin-top:2px;padding-bottom:4px;border-bottom:1px solid #c9c9c9;width:78px;position:relative}
  .agent__role::after{content:"";position:absolute;right:0;bottom:-1.5px;width:26px;height:2px;background:var(--red)}
  .card-contacts{position:absolute;left:27px;top:104px;list-style:none}
  .card-contacts li{display:flex;align-items:flex-start;gap:9px;margin-bottom:6px}
  .card-contacts .ico{flex:none;width:12px;height:12px;border-radius:2px;background:var(--red);display:flex;align-items:center;justify-content:center}
  .card-contacts .lines{font-size:7.4px;line-height:9.5px;color:var(--ink)}
  .ext{color:var(--red)}

  /* ---------- Card back ---------- */
  .card--back{left:720px;top:346px;width:411px;height:234px}
  .photo--city{left:-17px;top:32px;width:182px;height:182px;background:linear-gradient(180deg,#3f6fb6 0%,#8eb0d6 45%,#6f6a66 70%,#4c6b3f 100%)}
  .card--back .brand{position:absolute;left:206px;top:90px;font-size:21px}
  .card-web{position:absolute;left:170px;top:206px;display:flex;align-items:center;gap:7px;font-family:"Montserrat",Arial,sans-serif;font-size:8px;font-weight:600;color:var(--ink)}
  .card-web .dot{width:9px;height:9px;border-radius:50%;background:var(--red)}
  .card--back .badges{left:310px;top:194px;gap:5px}
  .card--back .badge{border-width:2px}
</style>
</head>
<body>
<main class="canvas">

  <!-- Letterhead -->
  <section class="letterhead" aria-label="Letterhead">
    <svg class="letterhead__top" width="475" height="36" viewBox="0 0 475 36" aria-hidden="true">
      <rect x="0" y="14" width="475" height="18" fill="var(--mist)"/>
      <polygon points="0,0 148,0 126,22 0,22" fill="var(--red)"/>
      <polygon points="148,0 475,0 475,14 134,14" fill="var(--charcoal)"/>
    </svg>

    <div class="brand"><span>Harborline</span><span>Realty</span></div>
    <div class="letterhead__date">Friday, 01/01/2018</div>

    <address class="recipient">
      <div class="recipient__to">TO</div>
      <div class="recipient__name">Dana Whitfield</div>
      <div>Human Resources</div>
      <div>Northfield Inc.</div>
      <div>2210 Cedar Row, Albany</div>
      <div>NY 12207 USA</div>
    </address>

    <div class="letter-body">
      <p>Thank you for meeting with our team last week to discuss the relocation plans for your staff. We have gathered a shortlist of homes near your new offices that fit the budget and timing you described. Each listing has been visited by one of our agents, and we have noted schools, commute times and local services for every address. We would be glad to arrange tours at a time that suits your schedule.</p>
      <p>Please find the full property packet enclosed with this letter for your review.</p>
      <p>We look forward to hearing from you soon.</p>
      <p>Our office can also help with temporary rentals, moving partners and mortgage contacts for employees arriving before their homes are ready. Just let us know how many families to expect and their preferred areas, and we will prepare a matching list within two business days.</p>
      <p>Every family will have a single agent as their main contact from the first call until closing day, so questions are answered quickly and nothing is missed along the way. We keep you updated weekly on progress.</p>
      <p>Thank you again for choosing our team to help with this move.</p>
    </div>

    <div class="signature">
      <div class="signature__name">Peter Hollis</div>
      <div class="signature__role">Broker</div>
    </div>

    <ul class="letter-contacts">
      <li><svg width="10" height="10" viewBox="0 0 10 10" aria-hidden="true"><path d="M2 1l2 2-1 1.2c.6 1.2 1.6 2.2 2.8 2.8L7 6l2 2-1.2 1.5C4.5 9.5.5 5.5.5 2.2z" fill="var(--red)"/></svg>413-826-4105</li>
      <li><svg width="10" height="10" viewBox="0 0 10 10" aria-hidden="true"><rect x="2" y="0.5" width="6" height="3" fill="var(--red)"/><rect x="0.5" y="3.5" width="9" height="4.5" rx="1" fill="var(--red)"/><rect x="2.5" y="7" width="5" height="2.5" fill="var(--red)"/></svg>417-945-2208</li>
      <li><svg width="10" height="10" viewBox="0 0 10 10" aria-hidden="true"><rect x="0.5" y="2" width="9" height="6.5" rx="1" fill="var(--red)"/><path d="M1 2.6l4 3 4-3" stroke="#fff" stroke-width=".9" fill="none"/></svg>contact@harborlinehomes.com</li>
    </ul>

    <div class="badges" aria-label="Association and listing badges">
      <div class="badge" style="width:36px;height:40px"></div>
      <div class="badge" style="width:48px;height:34px"></div>
      <div class="badge" style="width:42px;height:44px;border-radius:2px"></div>
    </div>

    <svg class="letterhead__footer" width="475" height="40" viewBox="0 0 475 40" aria-hidden="true">
      <rect x="0" y="16" width="475" height="24" fill="var(--charcoal)"/>
      <polygon points="300,16 475,16 475,6 310,6" fill="var(--mist)"/>
      <polygon points="395,6 475,6 475,24 412,24" fill="var(--red)"/>
      <polygon points="230,40 268,16 300,16 262,40" fill="var(--slate)"/>
    </svg>
    <div class="letterhead__web">
      <svg width="11" height="10" viewBox="0 0 11 10" aria-hidden="true"><rect x="0.7" y="0.7" width="9.6" height="6.6" fill="none" stroke="var(--red)" stroke-width="1.4"/><rect x="3.5" y="8.2" width="4" height="1.3" fill="var(--red)"/></svg>
      www.harborlinehomes.com
    </div>
  </section>

  <!-- Business card, front -->
  <section class="card card--front" aria-label="Business card front">
    <svg class="card__shapes" width="411" height="246" viewBox="0 0 411 246" aria-hidden="true">
      <polygon points="262,0 411,0 411,246 262,246 238,208 300,120 238,34" fill="var(--charcoal)"/>
      <polygon points="244,0 290,0 262,30" fill="var(--red)"/>
      <polygon points="290,0 340,0 330,12 300,12" fill="var(--red)"/>
      <polygon points="232,226 262,246 222,246" fill="var(--red)"/>
      <polygon points="398,60 411,48 411,92" fill="var(--red)"/>
    </svg>
    <div class="photo photo--agent" role="img" aria-label="Portrait photo of the broker in a dark suit reading documents in an office"></div>

    <div class="brand"><span>Harborline</span><span>Realty</span></div>

    <div class="agent">
      <div class="agent__name">Peter Hollis</div>
      <div class="agent__role">Broker</div>
    </div>

    <ul class="card-contacts">
      <li><span class="ico"><svg width="8" height="8" viewBox="0 0 10 10" aria-hidden="true"><path d="M2 1l2 2-1 1.2c.6 1.2 1.6 2.2 2.8 2.8L7 6l2 2-1.2 1.5C4.5 9.5.5 5.5.5 2.2z" fill="#fff"/></svg></span>
        <span class="lines">412-590-6637<br>415-203-9916 <span class="ext">Ext: 101</span></span></li>
      <li><span class="ico"><svg width="8" height="8" viewBox="0 0 10 10" aria-hidden="true"><rect x="2" y="0.5" width="6" height="3" fill="#fff"/><rect x="0.5" y="3.5" width="9" height="4" rx="1" fill="#fff"/><rect x="2.5" y="7" width="5" height="2.5" fill="#fff"/></svg></span>
        <span class="lines">419-562-0174</span></li>
      <li><span class="ico"><svg width="8" height="8" viewBox="0 0 10 10" aria-hidden="true"><rect x="0.5" y="2" width="9" height="6.5" rx="1" fill="#fff"/><path d="M1 2.6l4 3 4-3" stroke="var(--red)" stroke-width=".9" fill="none"/></svg></span>
        <span class="lines">peterhollis@harborlinehomes.com<br>www.harborlinehomes.com</span></li>
      <li><span class="ico"><svg width="8" height="8" viewBox="0 0 10 10" aria-hidden="true"><path d="M5 .5a3.3 3.3 0 0 1 3.3 3.3C8.3 6.3 5 9.5 5 9.5S1.7 6.3 1.7 3.8A3.3 3.3 0 0 1 5 .5z" fill="#fff"/><circle cx="5" cy="3.8" r="1.1" fill="var(--red)"/></svg></span>
        <span class="lines">457 Birchwood Lane<br>Millbrook, NY 12545</span></li>
    </ul>
  </section>

  <!-- Business card, back -->
  <section class="card card--back" aria-label="Business card back">
    <svg class="card__shapes" width="411" height="234" viewBox="0 0 411 234" aria-hidden="true">
      <polygon points="0,0 118,0 142,26 190,123 142,220 118,234 0,234" fill="var(--charcoal)"/>
      <polygon points="118,0 164,0 140,30" fill="var(--red)"/>
      <polygon points="150,40 176,20 176,72" fill="var(--slate)"/>
      <polygon points="150,206 180,192 176,234 140,234" fill="var(--red)"/>
    </svg>
    <div class="photo photo--city" role="img" aria-label="Photo of modern high-rise apartment towers beside a riverside park under a blue sky"></div>

    <div class="brand"><span>Harborline</span><span>Realty</span></div>

    <div class="card-web"><span class="dot"></span>www.harborlinehomes.com</div>

    <div class="badges" aria-label="Association and listing badges">
      <div class="badge" style="width:18px;height:20px"></div>
      <div class="badge" style="width:26px;height:17px"></div>
      <div class="badge" style="width:20px;height:20px;border-radius:2px"></div>
    </div>
  </section>

</main>
</body>
</html>
```